Larkspur Ridge Management - Business Cards

I need business cards. My current logo was designed by a designer at this site and I very much like and am happy with the results. I would like a business card that is trendy, unique, current yet professional. I deal with high net worth clients daily

Target Market(s)

Out of state investors looking to get into the rental market in Ohio

Industry/Entity Type

Property Management, Consulting

Contact Information for Business Card

Name, Title (Chief Financial Officer) office phone number (555) 817-3094 website address larkridgemgmt.example

Font styles to use
Sans Serif

Colors
0054AA
0677BA
7BADD7
CADEEF
E8F1F8
0094D4
00A9DD
6FCCEA
C7EBF8
E9F6FB
00AB8E
00BBA5
67D7C9
C6EFE9
E9F9F6

```html
<!DOCTYPE html>
<html lang="en">
<head>
<meta charset="utf-8">
<title>Larkspur Ridge Management – Business Cards</title>
<link rel="stylesheet" href="https://fonts.googleapis.com/css2?family=Mukta:wght@300;400;700&display=swap">
<style>
  :root {
    --backdrop: #5e5e60;
    --navy: #16284f;
    --navy-deep: #12213f;
    --paper: #f3f3f3;
    --pattern-light: #e6e6e6;
    --pattern-dark: #1b2e59;
    --accent-red: #c8202f;
    --ink-light: #ffffff;
  }
  * { box-sizing: border-box; margin: 0; padding: 0; }
  html, body { width: 1200px; height: 800px; overflow: hidden; }
  body {
    background: var(--backdrop);
    font-family: "Mukta", sans-serif;
    position: relative;
  }
  .card {
    position: absolute;
    top: 245px;
    width: 540px;
    height: 309px;
    overflow: hidden;
  }
  .card--front { left: 40px; background: var(--navy); }
  .card--back { left: 620px; background: var(--paper); }

  .pattern-area { position: absolute; left: 0; right: 0; top: 0; }
  .card--front .pattern-area {
    bottom: 0;
    background: radial-gradient(circle at 50% 45%, var(--pattern-dark), var(--navy) 70%);
  }
  .card--back .pattern-area {
    height: 196px;
    background: radial-gradient(circle at 50% 40%, var(--pattern-light), var(--paper) 75%);
  }

  .brand-name {
    position: absolute;
    left: 0; right: 0;
    display: flex;
    align-items: center;
    justify-content: center;
    gap: 10px;
    font-weight: 700;
    font-size: 24px;
    letter-spacing: 0.5px;
    text-transform: uppercase;
  }
  .brand-name__mark { width: 16px; height: 16px; }
  .card--front .brand-name { top: 135px; color: var(--ink-light); }
  .card--front .brand-name__mark { background: var(--ink-light); }
  .card--back .brand-name { top: 80px; color: var(--navy); }
  .card--back .brand-name__mark { background: var(--navy); }

  .info-band {
    position: absolute;
    left: 0; right: 0; bottom: 0;
    height: 113px;
    background: var(--navy-deep);
    color: var(--ink-light);
  }
  .accent-bar {
    position: absolute;
    left: 0; bottom: 12px;
    width: 4px; height: 40px;
    background: var(--accent-red);
  }
  .person { position: absolute; left: 40px; bottom: 22px; line-height: 1.15; }
  .person__name { font-weight: 700; font-size: 15px; }
  .person__title { font-weight: 300; font-size: 15px; }

  .contact-list {
    position: absolute;
    left: 300px; top: 16px;
    list-style: none;
    font-weight: 300;
    font-size: 13.5px;
    line-height: 1.5;
  }
  .contact-list li { display: flex; align-items: center; gap: 7px; }
  .contact-icon { width: 12px; height: 12px; flex: none; }
</style>
</head>
<body>

<section class="card card--front" aria-label="Business card front">
  <div class="pattern-area" role="img" aria-label="Faint repeating brand pattern on navy"></div>
  <div class="brand-name"><span class="brand-name__mark"></span>Larkspur Ridge Management</div>
</section>

<section class="card card--back" aria-label="Business card back">
  <div class="pattern-area" role="img" aria-label="Faint repeating brand pattern on white"></div>
  <div class="brand-name"><span class="brand-name__mark"></span>Larkspur Ridge Management</div>

  <div class="info-band">
    <span class="accent-bar"></span>
    <ul class="contact-list">
      <li>
        <svg class="contact-icon" viewBox="0 0 12 12" aria-hidden="true"><circle cx="6" cy="6" r="6" fill="#fff"/><path d="M3.6 3.2l1.2-.3.6 1.4-.7.5a4 4 0 0 0 1.6 1.6l.5-.7 1.4.6-.3 1.2c-2.3.1-4.4-2-4.3-4.3z" fill="#12213f"/></svg>
        (555) 817-3094 (Office)
      </li>
      <li>
        <svg class="contact-icon" viewBox="0 0 12 12" aria-hidden="true"><circle cx="6" cy="6" r="6" fill="#fff"/><rect x="3" y="4" width="6" height="4.2" fill="none" stroke="#12213f" stroke-width=".9"/><path d="M3 4l3 2.4L9 4" fill="none" stroke="#12213f" stroke-width=".9"/></svg>
        info@larkridgemgmt.example
      </li>
      <li>
        <svg class="contact-icon" viewBox="0 0 12 12" aria-hidden="true"><circle cx="6" cy="6" r="6" fill="#fff"/><circle cx="6" cy="6" r="3.2" fill="none" stroke="#12213f" stroke-width=".8"/><path d="M2.8 6h6.4M6 2.8c-1.6 1.8-1.6 4.6 0 6.4M6 2.8c1.6 1.8 1.6 4.6 0 6.4" fill="none" stroke="#12213f" stroke-width=".7"/></svg>
        larkridgemgmt.example
      </li>
    </ul>
    <div class="person">
      <p class="person__name">Name</p>
      <p class="person__title">Chief Financial Officer</p>
    </div>
  </div>
</section>

</body>
</html>
```